Wine Label Design

Organization name: Orvell Wine Company

My company is called Orvell Wine Company, I’m a wine importer and wholesaler who distributes wine domestically.

We are about to launch a line of three premium and one sparkling wine that we will wholesale to various retailers, wine stores, and restaurants for re-sale. The wines label will have “Dean Marlowe” I plan on having the labels the same and just changing the varietal as needed. My wine are made from premium grapes and will be marketed as a high end wine. My current label size is 3 1/2" wide by 5" in long and the labels can be on a solid background or transparent.

I would like the first label to be for my Cabernet Sauvignon, California, 2012, 750ML (for the size of the bottle) and ALC 13.8% BY VOL (for the alcohol content).

Colors: I am open to any and all designs that would alter my perception of what will be best!

Further:
Current label is boring and poorly done, so hopefully you designers can come up with something better

Industry/Entity Type

It Company

```html
<!DOCTYPE html>
<html lang="en">
<head>
<meta charset="utf-8">
<title>Dean Marlowe — Cabernet Sauvignon Label</title>
<link rel="stylesheet" href="https://fonts.googleapis.com/css2?family=Questrial&family=Great+Vibes&display=swap">
<style>
  :root {
    --charcoal: #262628;
    --navy: #0b3558;
    --gold: #c2a062;
    --gold-light: #f7e6b0;
    --gold-dark: #8f6c35;
    --white: #ffffff;
  }
  html, body {
    margin: 0;
    padding: 0;
    width: 840px;
    height: 1200px;
    overflow: hidden;
    background: var(--navy);
  }
  .label {
    position: relative;
    width: 840px;
    height: 1200px;
    background: var(--navy);
    overflow: hidden;
  }
  .label__header {
    position: absolute;
    left: 0; top: 0;
    width: 840px;
    height: 400px;
    background: var(--charcoal);
  }
  .gold-band {
    position: absolute;
    left: 0;
    width: 840px;
    height: 18px;
    background: linear-gradient(90deg, var(--gold-dark) 0%, var(--gold) 12%, var(--gold-light) 30%, var(--gold) 50%, var(--gold-light) 75%, var(--gold) 90%, var(--gold-dark) 100%);
  }
  .gold-band--top { top: 400px; }
  .gold-band--bottom { top: 1182px; }

  .vine-ornament {
    position: absolute;
    background: radial-gradient(ellipse at center, rgba(26, 79, 120, 0.55) 0%, rgba(26, 79, 120, 0) 70%);
  }
  .vine-ornament--left { left: -60px; top: 430px; width: 340px; height: 580px; }
  .vine-ornament--right { left: 500px; top: 750px; width: 400px; height: 440px; }

  .text-line {
    position: absolute;
    left: 0;
    width: 840px;
    margin: 0;
    text-align: center;
    font-weight: 400;
    line-height: 1;
    white-space: nowrap;
  }
  .brand {
    top: 164px;
    font-family: "Questrial", sans-serif;
    font-size: 76px;
    letter-spacing: 4px;
    color: var(--gold);
  }
  .varietal {
    font-family: "Questrial", sans-serif;
    font-size: 92px;
    letter-spacing: 1px;
    color: var(--gold);
  }
  .varietal--first { top: 497px; }
  .varietal--second { top: 616px; }
  .varietal__initial { font-size: 1.2em; line-height: 0; }

  .appellation {
    top: 727px;
    font-family: "Great Vibes", cursive;
    font-size: 84px;
    letter-spacing: 1px;
    color: var(--white);
  }
  .vintage {
    top: 831px;
    font-family: "Questrial", sans-serif;
    font-size: 64px;
    color: var(--gold);
  }
  .volume {
    top: 1039px;
    font-family: "Questrial", sans-serif;
    font-size: 40px;
    color: var(--white);
  }
  .alcohol {
    top: 1119px;
    font-family: "Questrial", sans-serif;
    font-size: 33px;
    color: var(--white);
  }
</style>
</head>
<body>
  <div class="label">
    <div class="label__header"></div>
    <div class="gold-band gold-band--top"></div>

    <div class="vine-ornament vine-ornament--left" role="img" aria-label="Faint scrolling grapevine ornament with grape clusters"></div>
    <div class="vine-ornament vine-ornament--right" role="img" aria-label="Faint scrolling grapevine ornament with grape clusters"></div>

    <h1 class="text-line brand">DEAN MARLOWE</h1>

    <h2 class="text-line varietal varietal--first"><span class="varietal__initial">C</span>ABERNET</h2>
    <h2 class="text-line varietal varietal--second"><span class="varietal__initial">S</span>AUVIGNON</h2>

    <div class="text-line appellation">California</div>
    <div class="text-line vintage">2012</div>
    <div class="text-line volume">750 ML</div>
    <div class="text-line alcohol">ALC 13.8% BY VOL</div>

    <div class="gold-band gold-band--bottom"></div>
  </div>
</body>
</html>
```